Copper Lantern Greeting Cards

I need a line of greeting cards designed that revolve around wine.
What I'm hoping for is that each card will include a bottle of wine on the front and some other cool, pretty, interesting design. So the main focus is of course the bottle (or perhaps a glass) of wine and the rest can be more esoteric - not necessarily anything concrete... shapes, lines, swirls, whatever - I'm open to ideas.
For the inside I'd like just a narrow border consisting of grape vines.

I've written a bout 15 cards so far and I am hoping to find someone (maybe a fellow wine-lover) in sync with what I envision. To start, I am looking for one design for the front of a card that goes along with the saying...
I Searched High and Merlot

The inside will say...
My heart had journeyed far and wide
To find someone who made it skip beat
And then came you and suddenly
I was swept right off my feet

I love you!

So, that's pretty much sums up the project.

```html
<!DOCTYPE html>
<html lang="en">
<head>
<meta charset="utf-8">
<title>I Searched High and Merlot — Greeting Card Front</title>
<link rel="stylesheet" href="https://fonts.googleapis.com/css2?family=Dancing+Script:wght@700&family=Great+Vibes&display=swap">
<style>
  :root {
    --paper: #ede4cf;
    --wine: #8a3a48;
    --plum: #5c1d3b;
    --vine-tint: #d9c2b6;
    --vine-deep: #c7a2a0;
    --bottle-tint: #cfc6bb;
  }
  html, body {
    margin: 0;
    padding: 0;
    width: 857px;
    height: 1200px;
    overflow: hidden;
    background: var(--paper);
  }
  .card {
    position: relative;
    width: 857px;
    height: 1200px;
    background: var(--paper);
    overflow: hidden;
  }
  .card-frame,
  .card-title {
    position: absolute;
    inset: 0;
  }
  .card-title {
    margin: 0;
    font-size: inherit;
    font-weight: inherit;
  }
  .vine-art {
    position: absolute;
    border-radius: 40% 40% 50% 50%;
  }
  .vine-art--left {
    left: 60px; top: 45px; width: 250px; height: 365px;
    background: radial-gradient(ellipse at 40% 55%, var(--vine-deep) 0%, var(--vine-tint) 45%, rgba(237,228,207,0) 75%);
  }
  .vine-art--right {
    left: 547px; top: 45px; width: 250px; height: 365px;
    background: radial-gradient(ellipse at 60% 55%, var(--vine-deep) 0%, var(--vine-tint) 45%, rgba(237,228,207,0) 75%);
  }
  .bottle-art {
    position: absolute;
    left: 401px; top: 76px; width: 56px; height: 205px;
    border-radius: 10px 10px 6px 6px;
    background: linear-gradient(90deg, var(--bottle-tint), #e3dbcf 60%, var(--bottle-tint));
  }
  .title-script {
    font-family: "Great Vibes", cursive;
    fill: var(--plum);
  }
  .title-brush {
    font-family: "Dancing Script", cursive;
    font-weight: 700;
    fill: var(--wine);
  }
</style>
</head>
<body>
  <main class="card">
    <svg class="card-frame" width="857" height="1200" viewBox="0 0 857 1200" aria-hidden="true">
      <polygon points="78,30 779,30 819,72 819,1093 744,1168 113,1168 38,1093 38,72"
               fill="none" stroke="var(--wine)" stroke-width="4"/>
      <polygon points="82,40 775,40 809,76 809,1089 740,1158 117,1158 48,1089 48,76"
               fill="none" stroke="var(--wine)" stroke-width="2"/>
    </svg>

    <div class="vine-art vine-art--left" role="img" aria-label="Drawn grape vine with leaves, tendrils and a hanging grape cluster"></div>
    <div class="vine-art vine-art--right" role="img" aria-label="Drawn grape vine with leaves, tendrils and a hanging grape cluster"></div>
    <div class="bottle-art" role="img" aria-label="Sketched wine bottle"></div>

    <h1 class="card-title">
      <svg width="857" height="1200" viewBox="0 0 857 1200">
        <text class="title-script" x="275" y="418" font-size="80" textLength="310" lengthAdjust="spacingAndGlyphs">I Searched</text>
        <text class="title-brush" x="190" y="700" font-size="300" textLength="500" lengthAdjust="spacingAndGlyphs">High</text>
        <text class="title-script" x="300" y="836" font-size="70" textLength="108" lengthAdjust="spacingAndGlyphs">and</text>
        <text class="title-brush" x="105" y="1000" font-size="270" textLength="635" lengthAdjust="spacingAndGlyphs">Merlot</text>
      </svg>
    </h1>
  </main>
</body>
</html>
```